"TR wanderer" Périple Transportation Company with vehicles not exceeding 9 seats. shuttle kil

Need a design full of freshness to make a trip relaxing drive, comfortable, safe, ideal for a trip with confidence. Punctuality. A positive visual impact, enter information about the company, a logo that stands out from other competitors but remains both simple and enjoyable ... Trust, punctuality, relaxing, stress. Generosity in the passenger transport service, mainly for airport shuttles between Paris and Normandy, but also any kind of distance, France and Europe, as long as there is a road we can go

Target Market(s)

Airport Shuttle Service and all distances for the companies and individuals

Industry/Entity Type

Transfer

Contact Information for Business Card

Société : TR Périple, Luc Barnier
Adresse : Rue Paul Dantier, Bâtiment KRP, 76420 Lillebonne, 0672418053, l.barnier@trperiple.fr

Font styles to use
Sans Serif

Colors

Designer to choose colors to be used in the design.

Requirements
Must have
• Company Information: Name: TR Périple Rue Paul Dantier KRP Building City: 76420 Lillebonne Phone: 0672418053 Email: l.barnier@trperiple.fr
Nice to have
• a card that lives with his time, good agreement with the times
Should not have
• too classic card's lack of a nursery stock, lack of alliance of colors

```html
<!DOCTYPE html>
<html lang="fr">
<head>
<meta charset="utf-8">
<title>TR Périple – Cartes de visite</title>
<link href="https://fonts.googleapis.com/css2?family=Questrial&display=swap" rel="stylesheet">
<style>
  :root {
    --stage: #ecebe8;
    --card: #f4f4f4;
    --card-edge: #e2e2e2;
    --ink: #4a4a4a;
    --ink-soft: #6b6b6b;
    --accent: #e07a2b;
    --shape: #e4e4e4;
  }
  * { margin: 0; padding: 0; box-sizing: border-box; }
  html, body { width: 1200px; height: 800px; overflow: hidden; }
  body {
    background: var(--stage);
    font-family: "Questrial", "Century Gothic", sans-serif;
    position: relative;
  }
  .card {
    position: absolute;
    top: 232px;
    width: 520px;
    height: 336px;
    background: var(--card);
    border: 1px solid var(--card-edge);
    box-shadow: 0 6px 18px rgba(0,0,0,0.10);
    overflow: hidden;
  }
  .card--front { left: 50px; }
  .card--back { left: 630px; }

  .brand {
    position: absolute;
    display: flex;
    align-items: center;
    gap: 10px;
    color: var(--ink);
    font-size: 30px;
    letter-spacing: 1px;
    white-space: nowrap;
  }
  .brand__mark {
    width: 18px; height: 18px;
    background: var(--accent);
  }
  .card--front .brand {
    left: 50%; top: 50%;
    transform: translate(-50%, -50%);
  }
  .card--back .brand {
    left: 250px; top: 62px;
    font-size: 24px;
  }
  .card--back .brand__mark { width: 14px; height: 14px; }

  .backdrop-shape {
    position: absolute;
    left: 60px; top: 120px;
    width: 230px; height: 230px;
    background: var(--shape);
  }

  .holder {
    position: absolute;
    left: 48px; top: 222px;
  }
  .holder__name {
    color: var(--accent);
    font-size: 32px;
    line-height: 1;
  }
  .holder__role {
    color: var(--ink-soft);
    font-size: 16px;
    margin-top: 6px;
  }

  .contact {
    position: absolute;
    left: 300px; top: 180px;
    list-style: none;
    color: var(--ink);
    font-size: 15px;
  }
  .contact__item {
    display: flex;
    align-items: center;
    gap: 8px;
    margin-bottom: 8px;
  }
  .contact__icon { width: 18px; height: 18px; flex: none; }
</style>
</head>
<body>

  <section class="card card--front" aria-label="Recto">
    <div class="brand">
      <span class="brand__mark"></span>
      <span class="brand__name">TR PÉRIPLE</span>
    </div>
  </section>

  <section class="card card--back" aria-label="Verso">
    <div class="backdrop-shape"></div>

    <div class="brand">
      <span class="brand__mark"></span>
      <span class="brand__name">TR PÉRIPLE</span>
    </div>

    <div class="holder">
      <p class="holder__name">Luc Barnier</p>
      <p class="holder__role">Manager</p>
    </div>

    <ul class="contact">
      <li class="contact__item">
        <svg class="contact__icon" viewBox="0 0 18 18" aria-hidden="true">
          <circle cx="9" cy="9" r="9" fill="#e07a2b"/>
          <path d="M6 4.5h2l.8 2.2-1.2.9a6 6 0 0 0 2.8 2.8l.9-1.2 2.2.8v2c0 .6-.5 1-1 1A8 8 0 0 1 5 5.5c0-.5.4-1 1-1z" fill="#fff"/>
        </svg>
        <span>0672418053</span>
      </li>
      <li class="contact__item">
        <svg class="contact__icon" viewBox="0 0 18 18" aria-hidden="true">
          <circle cx="9" cy="9" r="9" fill="#e07a2b"/>
          <rect x="4.5" y="6" width="9" height="6.5" rx="0.8" fill="none" stroke="#fff" stroke-width="1.2"/>
          <path d="M4.8 6.4 9 9.6l4.2-3.2" fill="none" stroke="#fff" stroke-width="1.2"/>
        </svg>
        <span>contact@trperiple.fr</span>
      </li>
    </ul>
  </section>

</body>
</html>
```